"End of year wishes" - Electronic card

Quenlax is a regulatory consulting company in the cosmetic sector. We provide premium services and have 12 years of experience.
Please visit our website for more information: https://quenlax.example
Like every year, we would like to send an electronic design to our clients and partners to wish them happy holidays. This year, we would like to share two good news with them: offer them a surprise (to be revealed later on) and invite them to visit our new brand new website. We relay on your talent and imagination for the design! We need something very professional, serious, beautiful and in line with our graphic layout (see our company website)

Target Market(s)

cosmetic brands

Industry/Entity Type

Cosmetics

Requirements
Must have
• The following statement should be included to the design:

We wish you a Happy Holiday and a Marvelous New Year 2021!
As December is the month of giving, we have a surprise for you. Please contact your dedicated Account Manager to find out more!

Good news never comes alone, we've also updated our website in order to serve you better. We hope you like it as much as we do.
Please enjoy the experience: www.quenlax.example

```html
<!DOCTYPE html>
<html lang="en">
<head>
<meta charset="utf-8">
<title>Quenlax — Season's Greetings 2021</title>
<link rel="stylesheet" href="https://fonts.googleapis.com/css2?family=Rubik:wght@400;500;700&display=swap">
<style>
  :root {
    --night: #151515;
    --night-soft: #242424;
    --lime: #8fd400;
    --lime-deep: #55a80a;
    --glow: #c8f03a;
    --ink: #222222;
    --paper: #ffffff;
  }
  * { margin: 0; padding: 0; box-sizing: border-box; }
  html, body {
    width: 900px; height: 1200px; overflow: hidden;
    background: var(--paper);
    font-family: "Rubik", Arial, sans-serif;
  }
  .card { position: relative; width: 900px; height: 1200px; overflow: hidden; }

  .hero {
    position: absolute; left: 0; top: 0; width: 900px; height: 540px;
    background: radial-gradient(ellipse at 40% 30%, var(--night-soft) 0%, var(--night) 70%);
  }
  .hero-illustration {
    position: absolute; left: 40px; top: 40px; width: 330px; height: 440px;
    background: radial-gradient(ellipse at 50% 55%, rgba(200,240,58,0.45) 0%, rgba(143,212,0,0.18) 40%, rgba(21,21,21,0) 72%);
  }
  .hero-curve { position: absolute; left: 0; top: 505px; width: 900px; height: 40px; }

  .greeting {
    position: absolute; left: 402px; top: 132px;
    font-weight: 500; font-size: 48px; line-height: 60px;
    color: var(--paper);
  }
  .greeting .accent { color: var(--lime); }

  .surprise {
    position: absolute; left: 98px; top: 594px; width: 705px;
    font-size: 22px; line-height: 30px; text-align: center; color: var(--ink);
  }
  .surprise .accent { color: var(--lime); font-weight: 500; }

  .news {
    position: absolute; left: 0; top: 750px; width: 900px; height: 450px;
    background: var(--lime);
  }
  .news-text {
    position: absolute; left: 105px; top: 80px; width: 690px;
    font-size: 22px; line-height: 28px; text-align: justify; color: var(--ink);
  }
  .news-text strong { font-weight: 500; }
  .site-button {
    position: absolute; left: 262px; top: 219px; width: 376px; height: 60px;
    background: var(--lime-deep); color: var(--paper);
    display: flex; align-items: center; justify-content: center;
    font-weight: 500; font-size: 27px; letter-spacing: 1px; text-decoration: none;
  }
  .brand-plate {
    position: absolute; left: 262px; top: 321px; width: 376px; height: 60px;
    background: var(--paper);
    display: flex; align-items: center; justify-content: center;
    font-weight: 700; font-size: 28px; color: var(--ink);
  }
</style>
</head>
<body>
<main class="card">
  <section class="hero">
    <div class="hero-illustration" role="img" aria-label="Glowing Christmas tree made of lime-green sparkling stars on a starry night sky"></div>
    <h1 class="greeting">
      We wish you a<br>
      <span class="accent">Happy Holiday</span> &amp;<br>
      a <span class="accent">Marvelous</span><br>
      <span class="accent">New Year 2021!</span>
    </h1>
    <svg class="hero-curve" viewBox="0 0 900 40" preserveAspectRatio="none" aria-hidden="true">
      <path d="M0 40 Q450 -20 900 40 Z" fill="#ffffff"/>
    </svg>
  </section>

  <p class="surprise">
    As <span class="accent">December</span> is the month of <span class="accent">giving</span>, we have a surprise for you. Please <span class="accent">contact</span> your dedicated <span class="accent">Account Manager</span> to find out more!
  </p>

  <section class="news">
    <p class="news-text">
      <strong>Good news</strong> never comes alone, we've also <strong>updated</strong> our website in order to serve you better. We hope you like it as much as we do. Please enjoy the experience:
    </p>
    <a class="site-button" href="https://quenlax.example">WWW.QUENLAX.EXAMPLE</a>
    <div class="brand-plate">quenlax</div>
  </section>
</main>
</body>
</html>
```